Tidewater Platform Research Circle

Hi, I am having a workshop at the beginning of June on the above topic and require the following:
I would like the following:
- PPT template in widescreen and regular format (these are really the same but just need but design just needs to be scalable). I like clean ppt templates showing the section but leaving much of the slide for actual content. I like clean no nonsense fonts (calibri, arial, etc)
- 3 fold brochure (stationary)
- poster template for 8.5"x11" and 11"x17" posters (stationary, I do not need a letterhead per se except for the workshop agenda.
- The added stationary and logo options I picked on the "Design Options" page should cover all of the above.

It is not for the https://bluewaveconsortium.ca/ but we are an academic led network from www.kvu.ca wanting to do collaborate and do work in the key areas of the Bluewave Consortium especially related to offshore oil and gas in the areas of: production optimization, automation, safety & risk, marine operations, communications and controls, human factors, remote leadership an teams.

Keywords: digital oilfield, offshore oil and gas, integrated operations, digitalization, TEL47, Vestrand digital oil and gas, integrated operations, remote and harsh (ice and icebergs) offshore oil and gas field development, automation in oil and gas

I am hoping that since its just a workshop and the development needs to be done within the kvu.ca/brandoff/web/PGhelp/ framework, so its really just a banner and/or the ppt/poster graphic can fit within the KVU Page Maker template. The creation we will do.

Giving an extension until tomorrow. Based on what I see now, we will need to work together a little bit to get what I want/need. Okay?

1 page

Serif
Sans Serif

3176b5
33a6d7
33b8a4

```html
<!DOCTYPE html>
<html lang="en">
<head>
<meta charset="utf-8">
<title>Tidewater Platform Research Circle – Presentation Template</title>
<link href="https://fonts.googleapis.com/css2?family=Open+Sans:wght@300;400;600;700;800&display=swap" rel="stylesheet">
<style>
  :root {
    --navy: #1d5f9e;
    --blue: #3176b5;
    --sky: #33a6d7;
    --teal: #1f9dbf;
    --mint: #33b8a4;
    --pale-mint: #8ccfc4;
    --pale-green: #bfe3c5;
    --ink: #222;
    --grey: #555;
    --line: #4a4a4a;
    --white: #fff;
  }
  * { box-sizing: border-box; margin: 0; padding: 0; }
  html, body { width: 1200px; height: 900px; overflow: hidden; background: var(--white); }
  body { font-family: "Open Sans", Arial, sans-serif; color: var(--ink); position: relative; }

  .slide {
    position: absolute; width: 412px; height: 233px; overflow: hidden;
    transform: scale(1.1719); transform-origin: 0 0; background: var(--white);
  }
  .slide--1 { left: 111px; top: 29px; }
  .slide--2 { left: 614px; top: 29px; }
  .slide--3 { left: 111px; top: 323px; }
  .slide--4 { left: 614px; top: 323px; }
  .slide--5 { left: 111px; top: 615px; }
  .slide--6 { left: 614px; top: 615px; }

  .abs { position: absolute; }
  .bg-svg { position: absolute; left: 0; top: 0; width: 412px; height: 233px; }

  .headline { position: absolute; font-weight: 400; font-size: 16px; color: var(--grey); white-space: nowrap; }
  .headline--light { color: var(--white); }

  .body-copy { position: absolute; font-size: 5.6px; line-height: 1.28; font-weight: 700; color: var(--ink); }
  .body-copy--center { text-align: center; }
  .body-copy--justify { text-align: justify; }
  .body-copy--white { color: var(--white); }

  /* Cover */
  .cover__bg { position: absolute; inset: 0; background: linear-gradient(135deg, #cfe9c4 0%, #8fcfc3 25%, #4ba9c9 55%, #2a7ec0 100%); }
  .cover__band { position: absolute; left: 0; top: 45px; width: 412px; height: 72px; background: rgba(31, 127, 170, 0.82); }
  .cover__title { position: absolute; left: 31px; top: 52px; color: var(--white); font-size: 23px; line-height: 1.1; font-weight: 300; }
  .cover__title strong { display: block; font-weight: 700; }
  .cover__sub { position: absolute; left: 265px; top: 170px; color: var(--white); font-size: 14px; font-weight: 300; }

  /* Side panel */
  .side-panel__title { position: absolute; left: 300px; top: 78px; color: var(--white); font-size: 16.5px; line-height: 1.3; font-weight: 300; }

  /* Columns */
  .column-dot { position: absolute; top: 79px; width: 46px; height: 46px; border-radius: 50%; background: var(--teal); }
  .column-rule { position: absolute; top: 63px; width: 1px; height: 137px; background: var(--line); }

  /* Tags */
  .tag { position: absolute; left: 28px; height: 17px; display: flex; align-items: center; gap: 10px; padding-left: 18px; color: var(--white); font-size: 10.5px; font-weight: 400; }
  .tag__icon { width: 13px; height: 13px; }

  /* Steps */
  .step { position: absolute; border-radius: 50%; color: var(--white); font-weight: 700; display: flex; align-items: center; justify-content: center; }

  /* Labels */
  .label { position: absolute; height: 9px; color: var(--white); font-size: 5px; font-weight: 700; display: flex; align-items: center; padding-left: 16px; }
</style>
</head>
<body>

<!-- Cover -->
<section class="slide slide--1">
  <div class="cover__bg" role="img" aria-label="Low-poly faceted background in soft green and blue tones"></div>
  <div class="cover__band"></div>
  <h1 class="cover__title">Presentation<strong>Template</strong></h1>
  <p class="cover__sub">Your Text Here</p>
</section>

<!-- Three columns + side panel -->
<section class="slide slide--2">
  <svg class="bg-svg" viewBox="0 0 412 233" aria-hidden="true">
    <defs>
      <linearGradient id="corner-green" x1="0" y1="0" x2="1" y2="1">
        <stop offset="0" stop-color="#d9efcf"/><stop offset="1" stop-color="#a9dcc8"/>
      </linearGradient>
    </defs>
    <polygon points="0,187 85,218 118,233 0,233" fill="url(#corner-green)" opacity="0.8"/>
    <rect x="291" y="0" width="121" height="233" fill="#1f9dbf"/>
    <polygon points="238,0 412,0 412,82 350,62 300,20" fill="#3a8fc6"/>
    <polygon points="291,0 412,0 412,78 340,40" fill="#1d5f9e"/>
    <polygon points="360,0 412,0 412,60" fill="#154a82"/>
  </svg>
  <h2 class="headline" style="left:92px; top:30px;">Your Headline</h2>
  <div class="column-dot" style="left:35px;"></div>
  <div class="column-dot" style="left:126px;"></div>
  <div class="column-dot" style="left:218px;"></div>
  <div class="column-rule" style="left:103px;"></div>
  <div class="column-rule" style="left:196px;"></div>
  <p class="body-copy body-copy--center" style="left:12px; top:136px; width:84px;">Lorem ipsum dolor sit amet, consectetur adipiscing elit, sed do eiusmod tempor incididunt ut labore et dolore magna aliqua. Ut enim ad minim veniam.</p>
  <p class="body-copy body-copy--center" style="left:110px; top:136px; width:80px;">Lorem ipsum dolor sit amet, consectetur adipiscing elit, sed do eiusmod tempor incididunt ut labore et dolore magna aliqua. Ut enim ad minim veniam.</p>
  <p class="body-copy body-copy--center" style="left:202px; top:136px; width:80px;">Lorem ipsum dolor sit amet, consectetur adipiscing elit, sed do eiusmod tempor incididunt ut labore et dolore magna aliqua. Ut enim ad minim veniam.</p>
  <p class="side-panel__title">Your Text<br>Here</p>
  <p class="body-copy body-copy--justify body-copy--white" style="left:300px; top:127px; width:102px;">Lorem ipsum dolor sit amet, consectetur adipiscing elit, sed do eiusmod tempor incididunt ut labore et dolore magna aliqua. Ut enim ad minim veniam. Sed ut perspiciatis unde omnis iste natus error sit voluptatem accusantium.</p>
</section>

<!-- Tag list -->
<section class="slide slide--3">
  <svg class="bg-svg" viewBox="0 0 412 233" aria-hidden="true">
    <defs>
      <linearGradient id="header-a" x1="0" y1="0" x2="1" y2="0">
        <stop offset="0" stop-color="#9ad3c9"/><stop offset="0.5" stop-color="#4fb0cc"/><stop offset="1" stop-color="#2a7ec0"/>
      </linearGradient>
    </defs>
    <polygon points="0,0 412,0 412,69 380,52 330,50 262,58 190,44 120,50 60,42 0,54" fill="url(#header-a)"/>
  </svg>
  <h2 class="headline headline--light" style="left:148px; top:10px;">Your Headline</h2>

  <div class="tag" style="top:67px; width:182px; background:#2a7ab5; clip-path:polygon(0 0,94% 0,100% 50%,94% 100%,0 100%,3% 50%);">
    <svg class="tag__icon" viewBox="0 0 14 14" aria-hidden="true"><circle cx="7" cy="8" r="5" fill="none" stroke="#fff" stroke-width="1.4"/><path d="M7 8V5.5M5.5 1.5h3M7 1.5v1.5" stroke="#fff" stroke-width="1.4"/></svg>
    Lorem Ipsum
  </div>
  <div class="tag" style="top:116px; width:167px; background:#3aa2cf; clip-path:polygon(0 0,94% 0,100% 50%,94% 100%,0 100%,3% 50%);">
    <svg class="tag__icon" viewBox="0 0 14 14" aria-hidden="true"><circle cx="7" cy="7" r="6" fill="none" stroke="#fff" stroke-width="1.2"/><circle cx="7" cy="7" r="3.5" fill="none" stroke="#fff" stroke-width="1.2"/><circle cx="7" cy="7" r="1.2" fill="#fff"/></svg>
    Dolor Sit Amet
  </div>
  <div class="tag" style="top:165px; width:149px; background:linear-gradient(90deg,#5fbcc0,#a6dcbd); clip-path:polygon(0 0,94% 0,100% 50%,94% 100%,0 100%,3% 50%);">
    <svg class="tag__icon" viewBox="0 0 14 14" aria-hidden="true"><circle cx="7" cy="7" r="6.5" fill="#fff"/><text x="7" y="10.5" text-anchor="middle" font-size="10" font-weight="700" fill="#6cc1bf" font-family="Open Sans, sans-serif">$</text></svg>
    Consectetur
  </div>

  <p class="body-copy body-copy--justify" style="left:231px; top:75px; width:152px;">Lorem ipsum dolor sit amet, consectetur adipiscing elit, sed do eiusmod tempor incididunt ut labore et dolore magna aliqua. Ut enim ad minim veniam, quis nostrud exercitation ullamco laboris nisi ut aliquip ex ea commodo consequat. Duis aute irure dolor in reprehenderit in voluptate velit esse cillum dolore eu fugiat nulla pariatur. Excepteur sint occaecat cupidatat non proident, sunt in culpa qui officia deserunt mollit anim id est laborum.</p>
  <p class="body-copy body-copy--justify" style="left:231px; top:155px; width:152px;">Lorem ipsum dolor sit amet, consectetur adipiscing elit, sed do eiusmod tempor incididunt ut labore et dolore magna aliqua. Ut enim ad minim veniam, quis nostrud exercitation ullamco.</p>
</section>

<!-- Cycle diagram -->
<section class="slide slide--4">
  <svg class="bg-svg" viewBox="0 0 412 233" aria-hidden="true">
    <defs>
      <linearGradient id="corner-green-2" x1="0" y1="0" x2="1" y2="1">
        <stop offset="0" stop-color="#d9efcf"/><stop offset="1" stop-color="#a9dcc8"/>
      </linearGradient>
    </defs>
    <polygon points="0,187 85,218 118,233 0,233" fill="url(#corner-green-2)" opacity="0.8"/>
    <rect x="291" y="0" width="121" height="233" fill="#1f9dbf"/>
    <polygon points="238,0 412,0 412,82 350,62 300,20" fill="#3a8fc6"/>
    <polygon points="291,0 412,0 412,78 340,40" fill="#1d5f9e"/>
    <polygon points="360,0 412,0 412,60" fill="#154a82"/>

    <path d="M95.1,72.5 A76 76 0 0 1 196.9,72.5 L163.4,109.7 A26 26 0 0 0 128.6,109.7 Z" fill="#2a7ab5"/>
    <path d="M202.5,78.1 A76 76 0 0 1 202.5,179.9 L165.3,146.4 A26 26 0 0 0 165.3,111.6 Z" fill="#3a9fcf"/>
    <path d="M196.9,185.5 A76 76 0 0 1 95.1,185.5 L128.6,148.3 A26 26 0 0 0 163.4,148.3 Z" fill="#55b0cc"/>
    <path d="M89.5,179.9 A76 76 0 0 1 89.5,78.1 L126.7,111.6 A26 26 0 0 0 126.7,146.4 Z" fill="#8ccfc4"/>

    <path d="M146,62 c-4,0 -6,3 -6,6 c0,4 6,10 6,10 s6,-6 6,-10 c0,-3 -2,-6 -6,-6 z" fill="#fff"/>
    <circle cx="146" cy="68" r="2" fill="#2a7ab5"/>
    <g fill="#fff"><rect x="190" y="111" width="2.5" height="6"/><rect x="194" y="108" width="2.5" height="9"/><rect x="198" y="105" width="2.5" height="12"/><rect x="202" y="102" width="2.5" height="15"/></g>
    <circle cx="146" cy="189" r="5" fill="none" stroke="#fff" stroke-width="3" stroke-dasharray="2.2 1.7"/>
    <circle cx="146" cy="189" r="2.5" fill="#fff"/>
    <path d="M96,114 h16 a4,4 0 0 0 0,-8 a5,5 0 0 0 -9,-2 a4,4 0 0 0 -7,3 a3.5,3.5 0 0 0 0,7 z" fill="#fff"/>
  </svg>
  <h2 class="headline" style="left:92px; top:13px;">Your Headline</h2>
  <p class="body-copy body-copy--center body-copy--white" style="left:120px; top:82px; width:52px; font-size:4.4px;">Lorem ipsum dolor sit amet, consectetur adipiscing elit.</p>
  <p class="body-copy body-copy--center body-copy--white" style="left:180px; top:124px; width:42px; font-size:4.4px;">Lorem ipsum dolor sit amet, adipiscing elit.</p>
  <p class="body-copy body-copy--center body-copy--white" style="left:124px; top:160px; width:44px; font-size:4.4px;">Lorem ipsum dolor sit amet, adipiscing elit.</p>
  <p class="body-copy body-copy--center body-copy--white" style="left:74px; top:124px; width:42px; font-size:4.4px;">Lorem ipsum dolor sit amet, adipiscing elit.</p>
  <p class="side-panel__title" style="top:66px;">Your Text<br>Here</p>
  <p class="body-copy body-copy--justify body-copy--white" style="left:300px; top:113px; width:102px;">Lorem ipsum dolor sit amet, consectetur adipiscing elit, sed do eiusmod tempor incididunt ut labore et dolore magna aliqua. Ut enim ad minim veniam. Sed ut perspiciatis unde omnis iste natus error sit voluptatem accusantium.</p>
</section>

<!-- Steps -->
<section class="slide slide--5">
  <svg class="bg-svg" viewBox="0 0 412 233" aria-hidden="true">
    <defs>
      <linearGradient id="header-b" x1="0" y1="0" x2="1" y2="0">
        <stop offset="0" stop-color="#9ad3c9"/><stop offset="0.5" stop-color="#4fb0cc"/><stop offset="1" stop-color="#2a7ec0"/>
      </linearGradient>
    </defs>
    <polygon points="0,0 412,0 412,69 380,52 330,50 262,58 190,44 120,50 60,42 0,54" fill="url(#header-b)"/>
    <g stroke="#4a4a4a" stroke-width="5">
      <line x1="97" y1="120" x2="140" y2="145"/>
      <line x1="200" y1="138" x2="236" y2="116"/>
      <line x1="275" y1="120" x2="315" y2="147"/>
    </g>
  </svg>
  <h2 class="headline headline--light" style="left:148px; top:10px;">Your Headline</h2>
  <div class="step" style="left:65px; top:88px; width:38px; height:38px; background:#2a7ab5; font-size:14px;">01</div>
  <div class="step" style="left:130px; top:128px; width:74px; height:74px; background:#33a0c9; font-size:26px;">02</div>
  <div class="step" style="left:233px; top:81px; width:46px; height:46px; background:#4fb0c6; font-size:18px;">03</div>
  <div class="step" style="left:310px; top:135px; width:54px; height:54px; background:#8ccfc4; font-size:20px;">04</div>
  <p class="body-copy body-copy--center" style="left:118px; top:86px; width:100px; font-weight:400;">Lorem ipsum dolor sit amet, consectetur adipiscing elit, sed do eiusmod tempor</p>
  <p class="body-copy body-copy--center" style="left:18px; top:139px; width:100px; font-weight:400;">Lorem ipsum dolor sit amet, consectetur adipiscing elit, sed do eiusmod tempor</p>
  <p class="body-copy body-copy--center" style="left:204px; top:147px; width:104px; font-weight:400;">Lorem ipsum dolor sit amet, consectetur adipiscing elit, sed do eiusmod tempor</p>
  <p class="body-copy body-copy--center" style="left:296px; top:100px; width:100px; font-weight:400;">Lorem ipsum dolor sit amet, consectetur adipiscing elit, sed do eiusmod tempor</p>
</section>

<!-- Idea slide -->
<section class="slide slide--6">
  <svg class="bg-svg" viewBox="0 0 412 233" aria-hidden="true">
    <defs>
      <linearGradient id="header-c" x1="0" y1="0" x2="1" y2="0">
        <stop offset="0" stop-color="#9ad3c9"/><stop offset="0.5" stop-color="#4fb0cc"/><stop offset="1" stop-color="#2a7ec0"/>
      </linearGradient>
    </defs>
    <polygon points="0,0 412,0 412,69 380,52 330,50 262,58 190,44 120,50 60,42 0,54" fill="url(#header-c)"/>
  </svg>
  <h2 class="headline headline--light" style="left:148px; top:10px;">Your Headline</h2>
  <div class="abs" role="img" aria-label="Light bulb illustration in teal and blue" style="left:44px; top:50px; width:122px; height:165px; border-radius:61px 61px 30px 30px; background:linear-gradient(180deg,#8ccfc4 0%,#7cc6c6 60%,#2f8fc4 100%);"></div>

  <div class="label" style="left:168px; top:79px; width:88px; background:#2a7ab5; clip-path:polygon(0 0,100% 0,92% 100%,0 100%);">LOREM IPSUM</div>
  <div class="label" style="left:279px; top:79px; width:92px; background:#55b0cc; clip-path:polygon(0 0,100% 0,92% 100%,0 100%);">LOREM IPSUM</div>
  <div class="label" style="left:168px; top:154px; width:88px; background:#3a9fcf; clip-path:polygon(0 0,100% 0,92% 100%,0 100%);">LOREM IPSUM</div>
  <div class="label" style="left:279px; top:154px; width:92px; background:#8ccfc4; clip-path:polygon(0 0,100% 0,92% 100%,0 100%);">LOREM IPSUM</div>

  <p class="body-copy" style="left:168px; top:94px; width:90px; font-weight:400;">Lorem ipsum dolor sit amet consectetur adipiscing elit, sed do eiusmod tempor</p>
  <p class="body-copy" style="left:279px; top:94px; width:90px; font-weight:400;">Lorem ipsum dolor sit amet consectetur adipiscing elit, sed do eiusmod tempor</p>
  <p class="body-copy" style="left:168px; top:169px; width:90px; font-weight:400;">Lorem ipsum dolor sit amet consectetur adipiscing elit, sed do eiusmod tempor</p>
  <p class="body-copy" style="left:279px; top:169px; width:90px; font-weight:400;">Lorem ipsum dolor sit amet consectetur adipiscing elit, sed do eiusmod tempor</p>
</section>

</body>
</html>
```